HIGH END MEDICAL/ANTI-AGING START-UP BROCHURE + BUSINESS CARDS

Fernridgewellnessco.example needs a brochure which details our two top selling products. The Vital Matrix Profile Review (VMP) coupled with the 4(16) Plan.

Here is some information about the VMP and the 4(16) plan. Please see our website for pictures and color.

VMP-Vital Matrix Profile and Fernridge
Fernridge Wellness Co is changing the way people look at health by bringing the focus back to the physical examination and patient centered care. It's our new, cutting edge system, Vital Matrix Profile, that allows us to have unparalleled patient outcomes. Vital Matrix Profile is a true deep dive into the individual. The protocol assesses, measures and tracking over 70 different bio-parameters such as hormone balance, tissue health, muscle mass, fat mass, frame mass, water content, water distribution, and acid/alkaline balance. This new analytics tool allows hyper individualized and customized weight loss and health programs to evolve in a new and never before seen way.

The 4(16) Plan
The 4(16) Cleanse program works by creating a full metabolic reset geared towards facilitation of hormone optimization and balance as well as toxicity and fat removal. Toxins are fat soluble and often need targeted nutritional strategy for long-term weight loss to occur; this is why many people do not lose weight even on calorie restricted diets with exercise plans until they use proper nutritional protocol. The 4(16) Cleanse allows for fat cells to be released and disposed of while at the same time adding deficient nutrients back into the tissues, helping you to not only lose weight, but reach optimal health and hormonal balance at the same time.

Target Market(s)

High-end and upscale clients looking for boutique medical services. We deal with clients mostly in executive level finance.

Industry/Entity Type

Medical

Contact Information for Business Card

-Must have our logo
-website (fernridgewellnessco.example)
-a space for our titles, "Dr. Lionel Waples, Founder" & "Rosalind Marchetti, Program Director"
-office phone number and our cell phone numbers (we will give you our cell phone numbers later)

Font styles to use
Serif
Sans Serif

Colors
0355a3
0493ce
00a990
ffffff
000000
919191
474747

Requirements
Must have
• Brochure and business cards must be VERY modern, creative and sophisticated.
Nice to have
• Usage of the company colors and logo in a new and interesting way.
Should not have
• Do not use colors outside of our logo + black + grey or white.
• Nothing cartoonish.

```html
<!DOCTYPE html>
<html lang="en">
<head>
<meta charset="utf-8">
<title>Fernridge Wellness Co – Tri-fold Brochure</title>
<link href="https://fonts.googleapis.com/css2?family=PT+Sans:ital,wght@0,400;0,700;1,400&family=PT+Sans+Narrow:wght@400;700&display=swap" rel="stylesheet">
<style>
  :root{
    --blue-deep:#2b559f;
    --blue-mid:#4670b6;
    --blue-soft:#6f8fc7;
    --brand-blue:#0355a3;
    --sky:#0493ce;
    --teal:#00a990;
    --grey:#919191;
    --grey-dark:#474747;
    --paper:#ffffff;
    --backdrop:#d9d9db;
    --body-blue:#3a5fa8;
  }
  html,body{margin:0;padding:0;width:837px;height:1200px;overflow:hidden;background:var(--backdrop);}
  body{position:relative;font-family:"PT Sans",sans-serif;}
  .sheet{position:absolute;background:var(--paper);box-shadow:0 10px 14px rgba(0,0,0,.28);overflow:hidden;}
  .sheet--outside{left:88px;top:37px;width:678px;height:526px;}
  .sheet--inside{left:86px;top:600px;width:680px;height:527px;}
  .sheet__art{position:absolute;inset:0;width:100%;height:100%;}
  .block{position:absolute;}
  .heading{font-family:"PT Sans Narrow",sans-serif;font-weight:400;margin:0;line-height:1.22;}
  .heading--light{color:var(--paper);font-size:13px;}
  .heading--blue{color:var(--blue-mid);font-size:13px;}
  .rule{display:block;width:84px;height:1.5px;background:var(--teal);margin-top:9px;}
  .copy{font-size:7.2px;line-height:10.1px;text-align:justify;margin:0 0 10px;}
  .copy--light{color:var(--paper);}
  .copy--blue{color:var(--body-blue);text-align:left;}
  .copy--dark{color:var(--grey-dark);}
  .copy--small{font-size:6.4px;line-height:8.2px;}
  .subhead{font-family:"PT Sans Narrow",sans-serif;font-weight:700;color:var(--teal);font-size:8.4px;margin:0 0 5px;}
  .brand{display:flex;align-items:center;gap:6px;font-weight:700;font-size:12px;}
  .brand__dot{width:16px;height:16px;border-radius:50%;flex:none;}
  .brand--main{color:var(--brand-blue);justify-content:center;}
  .brand--main .brand__dot{background:var(--teal);}
  .brand--reverse{color:var(--paper);opacity:.85;}
  .brand--reverse .brand__dot{background:var(--paper);}
  .contact{text-align:center;font-size:8.6px;line-height:12px;color:var(--body-blue);}
  .contact--teal{color:var(--teal);font-weight:700;}
  .contact__phone{display:inline-flex;align-items:center;gap:3px;}
  .tagline{color:var(--paper);font-size:11px;line-height:15px;text-transform:uppercase;margin:0;}
  .tab{position:absolute;height:32px;display:flex;align-items:center;padding-left:16px;box-sizing:border-box;
       background:linear-gradient(90deg,#ffffff 70%,#e4e7ec);border-radius:0 16px 16px 0;
       font-family:"PT Sans Narrow",sans-serif;color:var(--teal);font-size:14px;}
  .section-title{font-family:"PT Sans Narrow",sans-serif;color:var(--paper);font-size:14px;margin:0 0 12px;}
  .more{color:var(--teal);font-size:7.4px;margin:0;line-height:10px;}
  .more-sub{color:var(--paper);font-size:7.4px;margin:0;line-height:10px;}
</style>
</head>
<body>

<!-- Outside sheet -->
<section class="sheet sheet--outside">
  <svg class="sheet__art" viewBox="0 0 678 526" preserveAspectRatio="none" aria-hidden="false">
    <defs>
      <linearGradient id="gBlue" x1="0" y1="0" x2="0" y2="1">
        <stop offset="0" stop-color="#2b559f"/><stop offset="1" stop-color="#5a7fc0"/>
      </linearGradient>
      <linearGradient id="gBlueR" x1="0" y1="0" x2="1" y2="1">
        <stop offset="0" stop-color="#5b7fc0"/><stop offset="1" stop-color="#2b559f"/>
      </linearGradient>
      <linearGradient id="gPaper" x1="0" y1="0" x2="1" y2="0">
        <stop offset="0" stop-color="#eef1f6"/><stop offset=".5" stop-color="#ffffff"/><stop offset="1" stop-color="#f1f3f7"/>
      </linearGradient>
      <linearGradient id="gMeadow" x1="0" y1="0" x2="0" y2="1">
        <stop offset="0" stop-color="#e7eddc"/><stop offset=".45" stop-color="#b9cf8b"/><stop offset="1" stop-color="#7fa15a"/>
      </linearGradient>
      <linearGradient id="gCouple" x1="0" y1="0" x2="0" y2="1">
        <stop offset="0" stop-color="#c7d89d"/><stop offset=".5" stop-color="#e6e4dc"/><stop offset="1" stop-color="#90a9cf"/>
      </linearGradient>
    </defs>
    <!-- panel: why detox -->
    <rect x="0" y="0" width="221" height="526" fill="url(#gBlue)"/>
    <path d="M0,275 C70,268 170,300 221,370 L221,390 C170,330 70,300 0,300Z" fill="#7e9bd0" opacity=".55"/>
    <path role="img" aria-label="Photo: smiling couple cycling along a sunny woodland path" d="M0,300 C70,296 170,330 221,405 L221,526 L0,526Z" fill="url(#gMeadow)"/>
    <path d="M0,300 C70,296 170,330 221,405" fill="none" stroke="#ffffff" stroke-width="3"/>
    <!-- panel: why emphasis -->
    <rect x="221" y="0" width="218" height="526" fill="url(#gPaper)"/>
    <!-- panel: cover -->
    <rect role="img" aria-label="Photo: happy couple, woman riding piggyback on man in a green field" x="439" y="0" width="239" height="526" fill="url(#gCouple)"/>
    <path d="M439,230 C520,300 610,360 678,430 L678,526 L439,526Z" fill="#cfd4de"/>
    <path d="M439,250 C515,315 605,380 678,455 L678,526 L439,526Z" fill="url(#gBlueR)"/>
    <path d="M439,240 C518,307 608,370 678,442" fill="none" stroke="#ffffff" stroke-width="5"/>
  </svg>

  <div class="block" style="left:17px;top:27px;width:195px;">
    <h2 class="heading heading--light">Why We Chose Detox as our<br>Primary Method of Treatmen?</h2>
    <span class="rule"></span>
  </div>
  <div class="block" style="left:14px;top:84px;width:195px;">
    <p class="copy copy--light">An interesting study was published in the 90's and it talked about the signs and symptoms of chronic poisoning. The signs of chronic poisoning were found to be the same seen everyday in medical offices and homes around the country, fatigue, headaches, inability to lose weight and many more...</p>
    <p class="copy copy--light">Fernridge Wellness Co uses detoxification as a baseline for treatment. Conventional medicine looks to add and add substances and drugs into the body in order to elicit change.</p>
    <p class="copy copy--light">Fernridge Wellness Co has a different approach. We utilize the latest in detoxification and biotransformation techniques to help pull toxic substances out of the body. When toxins are eliminated from the body, energy systems work more efficiently and create a happier and healthier environment in the body.</p>
  </div>

  <div class="block" style="left:238px;top:28px;width:180px;">
    <h2 class="heading heading--blue">Why The Emphasis<br>on Removing Toxins?</h2>
    <span class="rule"></span>
  </div>
  <div class="block" style="left:234px;top:75px;width:184px;">
    <p class="copy copy--blue">There are over 80,000 registered chemicals in the atmosphere, and for the most part, the information and science is lacking in regards to how they affect the human body, as well as our environment. Toxins have been linked to almost every disease imaginable on some level or mechanism. Toxins are direct mitochondrial poisons, meaning they drastically affect how your body produces the energy it needs to live and thrive. Science over the past 20 years has identified a huge number of specific toxic compounds, ubiquitous to the environment that fall into the category of endocrine disruptors or excitotoxins. Those terms refer to toxins which either affect the brain, or the way your body produces and uses hormones. Once we are able to rid the body of toxicity, many ailments resolve themselves without pharmacological treatment or disease progression.</p>
  </div>

  <div class="block" style="left:221px;top:330px;width:218px;">
    <div class="brand brand--main"><span class="brand__dot"></span>Fernridge Wellness Co</div>
  </div>
  <div class="block contact" style="left:221px;top:418px;width:218px;">
    <div class="contact--teal"><span class="contact__phone"><svg width="9" height="9" viewBox="0 0 24 24"><circle cx="12" cy="12" r="11" fill="none" stroke="#00a990" stroke-width="2"/><path d="M8 6l2 0 1 3-1.5 1a7 7 0 0 0 4.5 4.5L15 13l3 1v2a1 1 0 0 1-1 1A11 11 0 0 1 7 7a1 1 0 0 1 1-1z" fill="#00a990"/></svg>(555) 014-2290</span></div>
    <div class="contact--teal" style="margin-top:3px;">Info@Fernridgewellnessco.example</div>
    <div style="margin-top:5px;">Fernridge Wellness Co<br>12 Linden Row Suite 310<br>Harborview NE, 00417</div>
    <div class="contact--teal" style="margin-top:10px;">www.fernridgewellnessco.example</div>
  </div>

  <div class="block" style="left:451px;top:375px;width:190px;">
    <div class="brand brand--reverse"><span class="brand__dot"></span>Fernridge Wellness Co</div>
  </div>
  <div class="block" style="left:451px;top:466px;width:200px;">
    <p class="tagline">The Vital Matrix Profile Review (VMP) coupled with the 4(16) Plan.</p>
  </div>
</section>

<!-- Inside sheet -->
<section class="sheet sheet--inside">
  <svg class="sheet__art" viewBox="0 0 680 527" preserveAspectRatio="none">
    <defs>
      <linearGradient id="gBlue2" x1="0" y1="0" x2="0" y2="1">
        <stop offset="0" stop-color="#4670b6"/><stop offset="1" stop-color="#2b559f"/>
      </linearGradient>
      <linearGradient id="gRunner" x1="0" y1="0" x2="1" y2="1">
        <stop offset="0" stop-color="#9fbb6e"/><stop offset=".55" stop-color="#e2cbb0"/><stop offset="1" stop-color="#c9d6a5"/>
      </linearGradient>
      <linearGradient id="gProduce" x1="0" y1="0" x2="1" y2="1">
        <stop offset="0" stop-color="#d9b99b"/><stop offset=".6" stop-color="#b98c6c"/><stop offset="1" stop-color="#6f9a4a"/>
      </linearGradient>
      <radialGradient id="gSkin" cx=".5" cy=".5" r=".6">
        <stop offset="0" stop-color="#f5ddd0"/><stop offset="1" stop-color="#d9ac95"/>
      </radialGradient>
    </defs>
    <!-- panel: VMP -->
    <rect x="0" y="0" width="229" height="527" fill="url(#gBlue2)"/>
    <path role="img" aria-label="Photo: woman jogging outdoors with earphones and music player" d="M0,0 L229,0 L229,200 C160,250 80,250 0,230Z" fill="url(#gRunner)"/>
    <path d="M0,230 C80,250 160,250 229,200" fill="none" stroke="#ffffff" stroke-width="3"/>
    <!-- panel: middle -->
    <rect x="229" y="0" width="223" height="527" fill="#ffffff"/>
    <path d="M229,285 C300,255 400,265 452,315 L452,330 C400,282 300,275 229,300Z" fill="#c9ced8"/>
    <path role="img" aria-label="Photo: smiling woman holding fresh vegetables" d="M229,300 C300,275 400,282 452,330 L452,527 L229,527Z" fill="url(#gProduce)"/>
    <!-- panel: plan -->
    <rect x="452" y="0" width="228" height="527" fill="url(#gBlue2)"/>
    <circle cx="623" cy="473" r="46" fill="#ffffff" opacity=".85"/>
    <circle role="img" aria-label="Photo: toned figure in white underwear, close crop" cx="623" cy="473" r="41" fill="url(#gSkin)"/>
  </svg>

  <div class="tab" style="left:0;top:264px;width:178px;">VMP-Vital Matrix Profile</div>
  <div class="block" style="left:14px;top:315px;width:198px;">
    <p class="copy copy--light">Fernridge Wellness Co is changing the way people look at health by bringing the focus back to the physical examination and patient centered care. It's our new, cutting edge system, Vital Matrix Profile, that allows us to have unparalleled patient outcomes.</p>
    <p class="copy copy--light">Vital Matrix Profile is a true deep dive into the individual. The protocol assesses, measures and tracking over 70 different bio-parameters such as hormone balance, tissue health, muscle mass, fat mass, frame mass, water content, water distribution, and acid/alkaline balance.</p>
    <p class="copy copy--light">This new analytics tool allows hyper individualized and customized weight loss and health programs to evolve in a new and never before seen way.</p>
  </div>
  <div class="block" style="left:14px;top:497px;width:198px;">
    <p class="more">More Details...</p>
    <p class="more-sub">Leanness &amp; Health</p>
  </div>

  <div class="block" style="left:240px;top:23px;width:200px;">
    <p class="copy copy--dark">The scientific community has held lean body composition as one of the 4 tenets in maintaining good health for decades. Yet, we are the fattest nation in the world. The weight loss industry is booming and failing all in the same. Lifestyle diseases are taking over our healthcare system with no definitive forms of treatment while at the same time, expensive drugs are failing our families, communities and nation. Why? The answer is lack of an effective way to assess, track and treat body composition.</p>
    <p class="copy copy--dark">The better your body composition and cellular health is, the better you feel, the better you look, and the better you can be a role model for those you care about. It might be considered vain to want to look great! If that's the case, then we at Fernridge Wellness Co are 100% OK with that. Whatever your reason for changing your body composition, weight loss, health or vanity, we're on board!</p>
    <p class="subhead">Being Lean for Health and Vanity = 's Healthy Vanity!</p>
    <p class="copy copy--dark copy--small">Dr. Lionel has coined the term "healthy vanity" to popularize the realization that looking and feeling good are often one in the same, that we shouldn't feel guilty for making and wanting our insides, and our outsides, to be healthy as well as aesthetically pleasing.</p>
  </div>

  <div class="tab" style="left:452px;top:19px;width:177px;">The 4(16) Plan</div>
  <div class="block" style="left:464px;top:69px;width:198px;">
    <p class="copy copy--light">The 4(16) Cleanse program works by creating a full metabolic reset geared towards facilitation of hormone optimization and balance as well as toxicity and fat removal.</p>
    <p class="copy copy--light">Toxins are fat soluble and often need targeted nutritional strategy for long-term weight loss to occur; this is why many people do not lose weight even on calorie restricted diets with exercise plans until they use proper nutritional protocol.</p>
    <p class="copy copy--light">The 4(16) Cleanse allows for fat cells to be released and disposed of while at the same time adding deficient nutrients back into the tissues, helping you to not only lose weight, but reach optimal health and hormonal balance at the same time.</p>
  </div>
  <div class="block" style="left:464px;top:272px;width:198px;">
    <h3 class="section-title">The 4(16) Cleanse</h3>
    <p class="copy copy--light">The 4(16) Cleanse is an intensive detoxification week followed by a 16-day maintenance program. All 4(16) programs are completely customized.</p>
    <p class="copy copy--light">Customization of patient programming is dependent upon results reported following the Vital Matrix Profile assessment. Following the intensive 4-day period Fernridge Wellness Co sherpas clients into the 16-day maintenance portion of the program. Specific diet and lifestyle counseling is given for these weeks to ensure the continued success of the patient.</p>
  </div>
</section>

</body>
</html>
```